Dietary supplement, Clean and simple.

Hi,
I’d like to talk about the project,

About us:
We are a dietary supplement (Vitamins, Minerals, amino acids etc.) company.
The goal is to have about 25 products at the end of this year. However, for this goal to be achieved we need a good label design to make our products represent our company values.
I’ll be here every day supporting your questions, we are fully committed to making the highest/best quality/customer experience possible.

About the design and our values:
- Professional (We are in the industry of professionalism and expertise. I would love to show we are competent at this, Id. Like to have the labels looks like we have done our research.)
- Efficient (White spacing, good use of the space available.)
- Simple (Straight forward, in 5 seconds they have to know what the product they have is/how functions. We’re trying to simplify it for the consumer.
- No distractions (the only visually “distracting” factor can be the vector art.)

The guidelines:
The goal is to have a universal design, with one element that changes (Vector art). I’ll attach a file/multiple files I think can show some visuals on what I’m looking for, and what parts of the design I think are good/bad.

Label size: 69x155mm (Front is 77.5mm)

Design whatever you think fits our image. You’re the design expert, all I care about is that it fits our company standards/image.

Use this color/font.
Font: Sans Serif
Main company color is Mind green #237D62 (Use this color for something in the design.)

What I thought would be cool/might looks ugly, who knows:
1. The front of the label: Should have 1 vector art, preferably in the top right corner. (That looks good in multiple colors. The vector can have multiple areas to color, I would prefer 2 main colors in the vector art. The interchangeable colors are used for multiple kinds of products.)
2. Text/product information on the left. The text that will have to be displayed:
- Product name for instance “Magnesium + B6”
- Description for the product for instance “Magnesium with ginger taste”
- Company name or logo. (Add ® behind it. We are soon to be trademark registered.)
3. We need to show the "daily intake" amount on the front and also the amount in the complete bottle. For instance, “Daily intake 1 capsule, 60 capsules”.
• You don’t have to design the backside of the label. After I chose a design, I’d like to chat and give specific information on what areas need to be assigned where. (Too complex because of the law.)
Updates

Hi, Please make the deadline 31 days total. I want designers to have the time to design. And not be rushed to finish it.

I want to extend the deadline because i feel like a slightly more medical look would be interesting. Hope you can come up with something!!

Target Market(s)

Dietary supplement consumers

Industry/Entity Type

Dietary supplements

Font styles to use
Sans Serif

Colors

Designer to choose colors to be used in the design.

Requirements
Must have
• Trademark icon "®" has to be at the top right after the company logo(text of logo)/name.

```html
<!DOCTYPE html>
<html lang="en">
<head>
<meta charset="utf-8">
<title>Magnesium + B6 Label</title>
<link href="https://fonts.googleapis.com/css2?family=Roboto:wght@400;500;700&display=swap" rel="stylesheet">
<style>
  :root {
    --canvas: #ffffff;
    --ink: #111111;
    --brand-green: #237d62;
    --wave-light: #c9ecd2;
    --wave-mid: #5cbf6e;
    --frame: #d6dcdc;
    --band: #eef6f6;
  }
  * { margin: 0; padding: 0; box-sizing: border-box; }
  html, body {
    width: 1200px;
    height: 1200px;
    overflow: hidden;
    background: var(--canvas);
    font-family: "Roboto", Arial, sans-serif;
    color: var(--ink);
  }
  .label {
    position: absolute;
    left: 50px;
    top: 355px;
    width: 1100px;
    height: 490px;
    border: 2px solid var(--frame);
    background: var(--canvas);
    overflow: hidden;
  }
  .front-panel {
    position: absolute;
    left: 0;
    top: 0;
    width: 550px;
    height: 100%;
  }
  .vector-art {
    position: absolute;
    left: 197px;
    top: 0;
    width: 354px;
    height: 330px;
    background: radial-gradient(ellipse at 65% 45%, var(--wave-mid) 0%, var(--wave-light) 45%, rgba(255,255,255,0) 75%);
    opacity: 0.8;
  }
  .brand {
    position: absolute;
    left: 52px;
    top: 172px;
    font-weight: 700;
    font-size: 34px;
    letter-spacing: 0.5px;
    color: var(--brand-green);
    line-height: 1;
  }
  .brand sup {
    font-size: 12px;
    vertical-align: top;
    margin-left: 2px;
  }
  .product-name {
    position: absolute;
    left: 52px;
    top: 260px;
    font-weight: 700;
    font-size: 38px;
    line-height: 1;
  }
  .product-description {
    position: absolute;
    left: 52px;
    top: 303px;
    font-weight: 400;
    font-size: 21px;
  }
  .category {
    position: absolute;
    left: 52px;
    top: 365px;
    font-weight: 700;
    font-size: 21px;
  }
  .dosage {
    position: absolute;
    left: 52px;
    top: 408px;
    font-weight: 400;
    font-size: 14px;
    line-height: 1.2;
    text-transform: uppercase;
  }
  .back-panel-title {
    position: absolute;
    left: 760px;
    top: 218px;
    font-size: 29px;
    font-weight: 400;
  }
  .bottom-band {
    position: absolute;
    left: 0;
    bottom: 0;
    width: 100%;
    height: 36px;
    background: var(--band);
  }
</style>
</head>
<body>
  <div class="label">
    <section class="front-panel">
      <div class="vector-art" role="img" aria-label="Flowing green line-wave vector art"></div>
      <div class="brand">Verdant Calm<sup>®</sup></div>
      <h1 class="product-name">MAGNESIUM + B6</h1>
      <p class="product-description">Magnesium with ginger taste</p>
      <p class="category">Dietary Supplement</p>
      <p class="dosage">Daily intake 1 capsule<br>60 capsules</p>
    </section>
    <p class="back-panel-title">BACK LABEL</p>
    <div class="bottom-band"></div>
  </div>
</body>
</html>
```